Business Card Design for a Personal Trainer

I need a business card design for my job as a personal trainer. It should have a unique, modern and exclusive design. On the front there should be only my logo with my name and my job. 0163/2918374 Tobias Kellinger Lindenfeldweg 14 80412 Munich Germany The most important contact information is the web adress. it can be bigger than the rest, but its not necessary. The card should be 8,5cmx5,5cm big. Font: Roboto. Colors: black, white, gray, 56c1ff.

```html
<!DOCTYPE html>
<html lang="de">
<head>
<meta charset="utf-8">
<title>Tobias Kellinger – Visitenkarte</title>
<link href="https://fonts.googleapis.com/css2?family=Roboto:wght@400;500&display=swap" rel="stylesheet">
<style>
  :root {
    --white: #ffffff;
    --panel-grey: #f1f1f1;
    --ink: #111111;
    --accent: #7fe0fa;
    --photo-dark: #2a2a2a;
    --photo-mid: #6b6b6b;
  }
  html, body {
    margin: 0;
    padding: 0;
    overflow: hidden;
    background: var(--white);
  }
  .card {
    position: relative;
    width: 1200px;
    height: 777px;
    overflow: hidden;
    background: var(--white);
    font-family: "Roboto", Arial, sans-serif;
    color: var(--ink);
  }
  .info-panel {
    position: absolute;
    left: 396px;
    top: 0;
    width: 804px;
    height: 627px;
    background: var(--panel-grey);
  }
  .portrait {
    position: absolute;
    left: 72px;
    top: 54px;
    width: 382px;
    height: 573px;
    background: linear-gradient(180deg, var(--photo-mid) 0%, var(--photo-dark) 45%, #3a3a3a 100%);
    border-radius: 150px 150px 0 0;
  }
  .name {
    position: absolute;
    left: 534px;
    top: 178px;
    margin: 0;
    font-size: 50px;
    font-weight: 500;
    line-height: 1;
  }
  .contact {
    position: absolute;
    left: 534px;
    top: 290px;
    margin: 0;
    padding: 0;
    list-style: none;
    font-size: 38px;
    font-weight: 400;
    line-height: 53.5px;
  }
  .contact li {
    display: flex;
    align-items: center;
    gap: 12px;
    white-space: nowrap;
  }
  .contact svg {
    width: 44px;
    height: 38px;
    fill: var(--accent);
    flex: none;
  }
  .web-band {
    position: absolute;
    left: 0;
    top: 627px;
    width: 1200px;
    height: 150px;
    background: var(--accent);
  }
  .website {
    position: absolute;
    left: 50px;
    top: 50px;
    display: flex;
    align-items: center;
    gap: 16px;
    color: var(--white);
    font-size: 43px;
    font-weight: 400;
  }
  .website svg {
    width: 48px;
    height: 44px;
  }
  .brand-name {
    position: absolute;
    right: 40px;
    top: 92px;
    color: var(--white);
    font-size: 30px;
    font-weight: 400;
    letter-spacing: 0.5px;
    white-space: nowrap;
  }
</style>
</head>
<body>
<div class="card">
  <div class="info-panel"></div>
  <div class="portrait" role="img" aria-label="Schwarz-weiß Porträt des Personal Trainers mit verschränkten Armen"></div>

  <h1 class="name">Tobias Kellinger</h1>
  <ul class="contact">
    <li>
      <svg viewBox="0 0 44 38" aria-hidden="true"><rect x="2" y="6" width="40" height="28" rx="3"/><path d="M2 9 L22 22 L42 9" fill="none" stroke="#f1f1f1" stroke-width="3"/></svg>
      t.kellinger@mailpost.de
    </li>
    <li>
      <svg viewBox="0 0 44 38" aria-hidden="true"><path d="M33 24c-3-1-5 0-6 2-5-2-9-6-11-11 2-1 3-3 2-6L15 3c-1-1-3-1-5 0C4 6 6 16 14 24s18 10 21 4c1-2 1-4-1-5z" transform="rotate(90 22 19)"/></svg>
      0163/2918374
    </li>
    <li>
      <svg viewBox="0 0 44 38" aria-hidden="true"><path d="M22 3 L42 20 L38 20 L38 36 L27 36 L27 25 L17 25 L17 36 L6 36 L6 20 L2 20 Z"/></svg>
      Lindenfeldweg 14
    </li>
    <li>80412 München</li>
  </ul>

  <div class="web-band">
    <div class="website">
      <svg viewBox="0 0 48 44" aria-hidden="true"><rect x="3" y="3" width="42" height="28" rx="3" fill="none" stroke="#ffffff" stroke-width="5"/><rect x="20" y="31" width="8" height="7" fill="#ffffff"/><rect x="12" y="37" width="24" height="4" rx="1" fill="#ffffff"/></svg>
      www.kellinger-training.de
    </div>
    <div class="brand-name">TOBIAS KELLINGER</div>
  </div>
</div>
</body>
</html>
```